Help our Velvet Parlour find our winning design! We're looking for a business card....

We’re a Velvet Parlour in NY specializing in custom-made cakes and unique desserts.
Our cakes combine flavor and art, each designed to match customer’s special event and theme.
We’d like a unique business card with a clean design that will combine French chic and artistic look & feel.
We’d like to differentiate ourselves from standard bakeries, please don’t offer cupcake images :-)
Our logo is peach-pink and brown and we’d love to use these colors ( . Another color that can be added is gold - or feel free to suggest!

Target Market(s)

Women, ages 25-55

Industry/Entity Type

Boutique

Contact Information for Business Card

Text on card:
Logo
Velvet Parlour by Nadia Fenwick

www.xxxxxxxx.com
xxx@xxxxx.com
(555) xxx-xxxx
F – xxxxxxxxxx
IG - xxxxxxxxx

Font styles to use
Sans Serif
Script

Requirements
Must have
• Logo
• Clean look
• French chic and artistic look & feel.
Nice to have
• Damask pattern
Should not have
• Cupcake images

```html
<!DOCTYPE html>
<html lang="en">
<head>
<meta charset="utf-8">
<title>Velvet Parlour – Business Card</title>
<link rel="stylesheet" href="https://fonts.googleapis.com/css2?family=Lobster&family=Play:wght@400;700&display=swap">
<style>
  :root {
    --cocoa: #864a22;
    --cocoa-deep: #6f3a18;
    --cocoa-soft: #9a5a2e;
    --caramel: #e2a862;
    --band: #dc9a52;
    --band-ink: #8a4a21;
    --logo-ink: #3a2416;
  }
  html, body {
    margin: 0;
    padding: 0;
    overflow: hidden;
    background: var(--cocoa);
  }
  .card {
    position: relative;
    width: 1200px;
    height: 747px;
    overflow: hidden;
    background: var(--cocoa);
    font-family: "Play", sans-serif;
  }
  .card p, .card h1, .card ul { margin: 0; padding: 0; }
  .backdrop {
    position: absolute;
    inset: 0;
    background:
      radial-gradient(ellipse 420px 300px at 330px 320px, rgba(170,110,65,0.35), transparent 70%),
      radial-gradient(ellipse 360px 280px at 860px 300px, rgba(165,105,60,0.3), transparent 70%),
      linear-gradient(180deg, var(--cocoa-soft) 0%, var(--cocoa) 60%, var(--cocoa-deep) 100%);
  }
  .brand-name {
    position: absolute;
    top: 138px;
    left: 0;
    width: 100%;
    text-align: center;
    font-family: "Play", sans-serif;
    font-weight: 400;
    font-size: 50px;
    line-height: 52px;
    letter-spacing: 2px;
    color: var(--logo-ink);
  }
  .tagline {
    position: absolute;
    top: 215px;
    left: 0;
    width: 100%;
    text-align: center;
    font-family: "Play", sans-serif;
    font-size: 15px;
    line-height: 18px;
    letter-spacing: 4px;
    color: var(--logo-ink);
  }
  .owner {
    position: absolute;
    top: 231px;
    left: 0;
    width: 100%;
    text-align: center;
    font-family: "Lobster", cursive;
    font-weight: 400;
    font-size: 36px;
    line-height: 45px;
    color: var(--caramel);
    text-shadow: 0 5px 6px rgba(40,18,4,0.55);
  }
  .owner span { display: block; }
  .rule {
    position: absolute;
    left: 294px;
    width: 554px;
    border-top: 2px dotted var(--caramel);
    opacity: 0.85;
  }
  .rule.top { top: 379px; }
  .rule.bottom { top: 457px; }
  .contact {
    position: absolute;
    left: 0;
    width: 100%;
    text-align: center;
    color: var(--caramel);
    font-size: 26px;
    line-height: 28px;
  }
  .contact.web { top: 390px; }
  .contact.phone { top: 475px; }
  .social-band {
    position: absolute;
    top: 522px;
    left: 0;
    width: 100%;
    height: 168px;
    background: var(--band);
    box-shadow: 0 -6px 10px rgba(40,18,4,0.35), 0 6px 10px rgba(40,18,4,0.45);
  }
  .social-list {
    position: absolute;
    top: 44px;
    left: 404px;
    list-style: none;
  }
  .social-item {
    display: flex;
    align-items: center;
    height: 41px;
    color: var(--band-ink);
    font-size: 27px;
  }
  .social-mark {
    width: 31px;
    height: 31px;
    border-radius: 6px;
    background: var(--band-ink);
    margin-right: 26px;
  }
</style>
</head>
<body>
  <main class="card">
    <div class="backdrop" role="img" aria-label="Soft, faded photograph of a decorated celebration cake in warm chocolate tones"></div>

    <p class="brand-name">Velvet Parlour</p>
    <p class="tagline">HANDCRAFTED WITH LOVE</p>

    <h1 class="owner">
      <span>Velvet Parlour</span>
      <span>By</span>
      <span>Nadia Fenwick</span>
    </h1>

    <div class="rule top"></div>
    <p class="contact web">www.VelvetParlourNY.com<br>nadia@VelvetParlourNY.com</p>
    <div class="rule bottom"></div>
    <p class="contact phone">(555) 210-4836</p>

    <section class="social-band">
      <ul class="social-list">
        <li class="social-item"><span class="social-mark"></span>VelvetParlourCakes</li>
        <li class="social-item"><span class="social-mark"></span>VelvetParlourCakes</li>
      </ul>
    </section>
  </main>
</body>
</html>
```